Falzflyer-Design für Softwareprodukte
Zielgruppe
Wir bieten mit unserer Produktlinie Veranta Softwareprodukte für Fluggesellschaften und touristische Unternehmen. Unsere Softwarelösungen sind ein Vertriebssystem für Airlines (Inventory), Prozess-basierte Automatisierungen, Buchungsschnittstellen und Datenanalysen. Weiterhin bieten wir diesen Unternehmen Custom Development und Beratungsdienstleistungen an.
Aufgabenstellung
Wir benötigen einen Falzflyer. Die Maße sind in einem Datenblatt von unserer Druckerei enthalten.
Weiterhin haben wir unser Logo und unserem Color Code hochgeladen. In einem pdf haben wir zusätzlich die Inhalte zusammengefasst (aussen und innen), die im Flyer aufgeführt werden sollen (noch nicht alles ist auf unserer Website verfügbar).
Einige Bilder, die wir auf der Website nutzen bzw. nutzen werden, findet ihr dort auch . Es kann aber gerne anderes Bildmaterial verwendet werden.
Wir überarbeiten gerade unsere Website und nutzen neben den unterschiedlichen Grautönen vorrangig #4b75e5, #00bac9 und folgende Schriftarten: Pragrati Narrow für Überschriften, Open Sans für Texte
Flyer wird ausschließlich in Englisch benötigt.

```html
<!DOCTYPE html>
<html lang="en">
<head>
<meta charset="utf-8">
<title>Veranta Trifold Flyer</title>
<link rel="stylesheet" href="https://fonts.googleapis.com/css2?family=Open+Sans:wght@400;600;700&family=Pragati+Narrow:wght@400;700&display=swap">
<style>
  :root {
    --stage: #d6d7d8;
    --paper: #f4f5f6;
    --paper-shade: #e9ebec;
    --teal-dark: #25788c;
    --teal: #2f97a6;
    --teal-light: #5cc0c9;
    --teal-text: #1f8a98;
    --indigo: #5466b4;
    --sky-photo-top: #a9c4d1;
    --sky-photo-mid: #6f95a6;
    --city-photo: #3d5a66;
    --ink-grey: #7d8a92;
  }
  * { box-sizing: border-box; margin: 0; padding: 0; }
  html, body { width: 838px; height: 1200px; overflow: hidden; }
  body {
    background: var(--stage);
    font-family: "Open Sans", Arial, sans-serif;
    position: relative;
  }

  .spread {
    position: absolute;
    left: 49px;
    width: 740px;
    height: 523px;
    background: var(--paper);
    box-shadow: 0 14px 30px rgba(0,0,0,.18);
    overflow: hidden;
  }
  .spread--inside { top: 40px; }
  .spread--outside { top: 637px; }

  .fold {
    position: absolute; top: 0; bottom: 0; width: 1px;
    background: rgba(0,0,0,.08);
    z-index: 5;
  }
  .fold--one { left: 246px; }
  .fold--two { left: 493px; }

  /* Inside spread */
  .tower-photo {
    position: absolute; left: 22px; top: 22px; width: 340px; height: 479px;
    background: linear-gradient(180deg, var(--sky-photo-top) 0%, var(--sky-photo-mid) 55%, var(--city-photo) 100%);
  }
  .teal-field {
    position: absolute; left: 300px; top: 40px; width: 440px; height: 440px;
    background:
      radial-gradient(circle at 30% 35%, rgba(92,192,201,.55) 0 28%, transparent 29%),
      radial-gradient(circle at 85% 90%, rgba(37,120,140,.7) 0 35%, transparent 36%),
      linear-gradient(135deg, var(--teal-dark) 0%, var(--teal) 55%, var(--teal-light) 100%);
  }
  .benefits-title {
    position: absolute; left: 300px; top: 112px;
    font-family: "Pragati Narrow", Arial, sans-serif;
    font-weight: 700; font-size: 104px; line-height: 1;
    color: #fff; letter-spacing: 2px;
    z-index: 3;
  }
  .benefit-card {
    position: absolute; background: var(--paper);
    z-index: 2; padding: 22px 18px;
  }
  .benefit-card--main { left: 290px; top: 205px; width: 200px; height: 230px; }
  .benefit-card--side { left: 518px; top: 190px; width: 222px; height: 170px; padding-top: 14px; }
  .benefit-list { list-style: none; }
  .benefit-list li {
    position: relative; padding-left: 16px; margin-bottom: 9px;
    font-size: 11.5px; line-height: 1.25; color: var(--teal-text);
  }
  .benefit-list li::before {
    content: "→"; position: absolute; left: 0; top: 0; font-weight: 700;
  }
  .benefit-list strong { font-weight: 700; color: #1a7483; }

  /* Outside spread */
  .city-photo {
    position: absolute; left: 22px; top: 22px; width: 210px; height: 479px;
    background: linear-gradient(180deg, #4e6f7d 0%, #86a3ae 45%, #c9b8b4 52%, #3a5560 70%, #2e4650 100%);
  }
  .contact-panel { position: absolute; left: 266px; top: 0; width: 227px; height: 100%; }
  .plane-icon { position: absolute; left: 10px; top: 92px; width: 46px; height: 46px; }
  .contact-title {
    position: absolute; left: 10px; top: 146px;
    font-family: "Pragati Narrow", Arial, sans-serif;
    font-weight: 700; font-size: 44px; letter-spacing: 1px;
    color: var(--indigo);
  }
  .contact-lead {
    position: absolute; left: 10px; top: 300px;
    font-weight: 700; font-size: 14px; color: var(--indigo);
  }
  .contact-address {
    position: absolute; left: 10px; top: 326px;
    font-style: normal; font-size: 12px; line-height: 1.3; color: var(--teal-text);
  }
  .contact-phone {
    position: absolute; left: 10px; top: 392px;
    font-weight: 700; font-size: 17px; color: var(--teal-text);
  }
  .brand-panel { position: absolute; left: 513px; top: 0; width: 210px; height: 100%; }
  .brand-name {
    position: absolute; left: 0; top: 150px;
    font-size: 32px; font-weight: 400; color: var(--ink-grey); letter-spacing: 1px;
  }
  .brand-goal {
    position: absolute; left: 0; top: 225px; width: 200px;
    font-weight: 700; font-size: 13px; line-height: 1.35; color: var(--teal-light);
  }
  .brand-job {
    position: absolute; left: 0; top: 290px; width: 200px;
    font-weight: 700; font-size: 13px; line-height: 1.35; color: var(--indigo);
  }
</style>
</head>
<body>

<section class="spread spread--inside" aria-label="Flyer inside">
  <div class="tower-photo" role="img" aria-label="Photo of a television tower above a city under a cloudy sky"></div>
  <div class="teal-field"></div>
  <h1 class="benefits-title">BENEFITS</h1>

  <div class="benefit-card benefit-card--main">
    <ul class="benefit-list">
      <li><strong>Maximize</strong> your revenue</li>
      <li><strong>Make</strong> manual effort obsolete and reduce your distribution cost</li>
      <li><strong>Use</strong> your competitive advantage</li>
      <li><strong>Focus</strong> on business processes</li>
      <li><strong>Deploy</strong> Veranta within two hours</li>
    </ul>
  </div>

  <div class="benefit-card benefit-card--side">
    <ul class="benefit-list">
      <li><strong>Customize</strong> Veranta quick and easy</li>
      <li><strong>Eliminate</strong> complexity and benefit from our integration</li>
      <li><strong>Improve</strong> your innovation capabilities and provide direct access</li>
      <li><strong>Pay-as-you-go</strong> with no huge upfront costs (SaaS &amp; PaaS)</li>
    </ul>
  </div>

  <span class="fold fold--one"></span>
  <span class="fold fold--two"></span>
</section>

<section class="spread spread--outside" aria-label="Flyer outside">
  <div class="city-photo" role="img" aria-label="Photo of a city skyline at dusk under heavy clouds"></div>

  <div class="contact-panel">
    <svg class="plane-icon" viewBox="0 0 48 48" aria-hidden="true">
      <path fill="#5466b4" d="M4 22h16L12 6h6l14 16h10a3 3 0 0 1 0 6H32L18 44h-6l8-16H4l-2-3 2-3z"/>
    </svg>
    <h2 class="contact-title">CONTACT</h2>
    <p class="contact-lead">Get in touch with us</p>
    <address class="contact-address">
      Skyvantra GmbH<br>
      Kastanienallee 7b<br>
      12045 Berlin<br>
      Germany
    </address>
    <p class="contact-phone">+49 170 55 42 981</p>
  </div>

  <div class="brand-panel">
    <p class="brand-name">Skyvantra</p>
    <p class="brand-goal">Unifying Touristic and Airline Business is our Goal.</p>
    <p class="brand-job">Breaking the Technology Gap is our Job.</p>
  </div>

  <span class="fold fold--one"></span>
  <span class="fold fold--two"></span>
</section>

</body>
</html>
```